Business Card Design Project

We're an orthopaedic office, and our colors are blue white and balck. Dealing with physicians and healthcare execs, I'd like this card to have a classy, yet overpowering wow factor.

Here are a couple of cards I like that are close to what I'm looking for:
http://www.pixelbazaro.com/design/392047
http://www.pixelbazaro.com/design/286390

Industry/Entity Type

Healthcare

```html
<!DOCTYPE html>
<html lang="en">
<head>
<meta charset="utf-8">
<title>Central Ridge – Business Card</title>
<link rel="stylesheet" href="https://fonts.googleapis.com/css2?family=Open+Sans:wght@300;400&family=Ubuntu+Mono&display=swap">
<style>
  :root {
    --page: #e6e7ea;
    --navy-deep: #05071c;
    --navy: #0d1240;
    --bone-light: #d9dee6;
    --bone-mid: #8c96a8;
    --accent-blue: #4b50d6;
    --ink-white: #ffffff;
    --ink-soft: #e3e6ee;
  }
  html, body {
    margin: 0;
    width: 1200px;
    height: 1023px;
    overflow: hidden;
    background: var(--page);
  }
  .business-card {
    position: absolute;
    left: 75px;
    top: 211px;
    width: 1050px;
    height: 600px;
    border-radius: 6px;
    overflow: hidden;
    background: linear-gradient(100deg, var(--navy) 0%, var(--navy-deep) 100%);
    box-shadow: 0 18px 40px rgba(0,0,0,0.25);
  }
  .xray-image {
    position: absolute;
    inset: 0;
    background:
      radial-gradient(ellipse 420px 300px at 420px 250px, var(--bone-light) 0%, rgba(190,198,212,0.85) 35%, rgba(100,110,135,0.5) 65%, rgba(13,18,64,0) 100%),
      radial-gradient(ellipse 380px 220px at 720px 80px, rgba(170,178,196,0.7) 0%, rgba(13,18,64,0) 100%),
      linear-gradient(100deg, #2a3050 0%, var(--navy) 55%, var(--navy-deep) 100%);
  }
  .brand {
    position: absolute;
    left: 60px;
    top: 220px;
    display: flex;
    align-items: center;
    gap: 34px;
  }
  .brand-mark {
    width: 130px;
    height: 130px;
    border-radius: 50%;
    background: var(--accent-blue);
    flex: none;
  }
  .brand-name {
    font-family: "Open Sans", sans-serif;
    font-weight: 300;
    font-size: 84px;
    line-height: 1;
    letter-spacing: 1px;
    color: var(--ink-white);
    margin: 0;
  }
  .brand-tagline {
    font-family: "Open Sans", sans-serif;
    font-weight: 300;
    font-size: 32px;
    line-height: 1.1;
    color: var(--ink-white);
    margin: 8px 0 0 4px;
  }
  .contact {
    position: absolute;
    right: 48px;
    bottom: 40px;
    text-align: left;
    font-family: "Ubuntu Mono", monospace;
    font-size: 27px;
    line-height: 1.35;
    color: var(--ink-soft);
  }
  .contact p { margin: 0; }
  .contact .person { margin-bottom: 4px; }
</style>
</head>
<body>
  <div class="business-card">
    <div class="xray-image" role="img" aria-label="Blue-toned X-ray of a knee joint filling the card background"></div>

    <div class="brand">
      <div class="brand-mark"></div>
      <div>
        <h1 class="brand-name">CENTRAL RIDGE</h1>
        <p class="brand-tagline">Orthopaedic &amp; Sports<br>Medicine Center</p>
      </div>
    </div>

    <div class="contact">
      <p class="person">Darren Holloway - CEO</p>
      <p>(318) 555-0142</p>
      <p>dholloway@centralridgeortho.com</p>
      <p>2170 Linden Ave., Riverton, LA 70555</p>
    </div>
  </div>
</body>
</html>
```